Business Card and Stationary Design

After the successful redesign of our logo we are wanting to follow suite and create a new business card and stationary design!

New Logo is attached, information required on the business card should contain a mixture of the following but layout/arrangement is up to the designer.

Happy if the national provider number and abn are on the back, and happy for them to be smaller than the rest.

I am also happy to receive single sided or weird and wonderful designs.

Name
Title
National Provider Number 7192
ABN 53 614 289 117
Level 1, 214 Garrow Street
Brackenvale NSW 2316
Ph: 1300 587 902
Mobile: 0438 761 205
name@ironquillbuild.com.au
www.ironquillbuild.com.au

Target Market(s)

Professionals, Peers, Students, Suppliers...

Industry/Entity Type

Construction

Contact Information for Business Card

Listed in project description

Font styles to use
Other font styles liked:
• Century Gothic

Colors
0455a3
3176b5
ffffff

Requirements
Must have
• Professional Design, same color scheme as our logo
Nice to have
• Something that sets our apart from everyone else would be fantastic, open to size and shape and layout options, as long as they present professionally.
• Open to raised/embossed text, alternative materials, custom sizes, clear material
Should not have
• The color orange

```html
<!DOCTYPE html>
<html lang="en">
<head>
<meta charset="utf-8">
<title>Ironquill Build – Stationery Set</title>
<link href="https://fonts.googleapis.com/css2?family=Questrial&family=Roboto:wght@400;700&family=Pinyon+Script&display=swap" rel="stylesheet">
<style>
:root{
  --navy:#1e3a80;
  --blue:#0455a3;
  --ink:#555b66;
  --rule:#8d9097;
  --paper:#ffffff;
  --paper-shade:#f4f4f5;
  --board:#e3e3e4;
  --clear:#f7f8fa;
}
*{margin:0;padding:0;box-sizing:border-box}
html,body{width:1200px;height:924px;overflow:hidden;background:var(--board)}
body{position:relative;font-family:"Roboto",Arial,sans-serif;color:var(--ink)}
.sheet{position:absolute;background:linear-gradient(135deg,var(--paper),var(--paper-shade));box-shadow:0 1px 4px rgba(0,0,0,.18)}
.logo{position:absolute;display:flex;align-items:center;gap:3px;white-space:nowrap}
.logo .mark{width:9px;height:9px;background:var(--navy)}
.logo .name{font-family:"Questrial",Arial,sans-serif;color:var(--navy);font-size:12px;line-height:1;letter-spacing:.1px}
.logo.white .mark{background:#fff}
.logo.white .name{color:#fff}
.contact{position:absolute;font-size:5px;line-height:6px;color:var(--ink);border-left:1px solid #c7c8cc;padding-left:6px;white-space:nowrap}
.contact span{display:block}
.contact span::before{content:"";display:inline-block;width:3px;height:3px;background:var(--navy);border-radius:50%;margin-right:4px;vertical-align:middle}
.address{position:absolute;font-size:4.6px;line-height:5.6px;color:var(--ink);white-space:nowrap}
.footer{position:absolute;left:0;right:0;text-align:center;font-size:4.6px;line-height:6px;color:var(--ink);border-top:1px solid var(--rule);padding-top:9px;white-space:nowrap}
.person{position:absolute;font-size:5px;line-height:6px;white-space:nowrap}
.person b{display:block;font-size:6.4px;color:var(--navy);font-weight:700}
.letter-body{position:absolute;left:27px;top:121px;width:260px;font-size:5px;line-height:6.7px;color:#6a6e76}
.letter-body p{margin-bottom:7px}
.salutation{font-size:8px;line-height:10px;margin-bottom:14px;color:var(--ink)}
.signature{position:absolute;left:24px;top:301px;width:56px;height:22px;background:#e7ecf5;border-radius:3px}
.band{position:absolute;background:var(--navy)}
.clear-card{position:absolute;left:433px;top:54px;width:174px;height:98px;background:var(--clear);border:1px solid #c9ccd2;box-shadow:0 1px 4px rgba(0,0,0,.12)}
.notebook-lines{position:absolute;left:25px;right:28px;top:62px;height:285px;background:repeating-linear-gradient(180deg,transparent 0 17px,#a7a9ae 17px 18px)}
.spiral{position:absolute;left:-4px;top:12px;width:12px;height:370px;background:repeating-linear-gradient(180deg,#3a3d44 0 2px,transparent 2px 8px)}
.compliments{position:absolute;left:0;right:0;top:57px;text-align:center;font-family:"Pinyon Script",cursive;font-size:29px;color:var(--navy)}
</style>
</head>
<body>

<section class="sheet letterhead" style="left:41px;top:38px;width:309px;height:436px">
  <div class="logo" style="left:27px;top:37px"><i class="mark"></i><span class="name">ironquill build</span></div>
  <div class="contact" style="left:207px;top:33px">
    <span>1300 587 902</span><span>name@ironquillbuild.com.au</span><span>www.ironquillbuild.com.au</span>
  </div>
  <div class="letter-body">
    <p class="salutation">Dear Mr. Reeve,</p>
    <p>Lorem ipsum dolor sit amet, consectetur adipiscing elit. Donec orci purus, luctus vitae dignissim eu, iaculis sed purus. Vivamus faucibus, ipsum nec aliquet viverra, leo mauris condimentum ligula, sit amet sagittis enim ligula quis arcu. Nam egestas tortor id nisi porttitor mattis. In tortor ante, ultricies in suscipit a, tempus non massa. Vivamus et auctor mi. Fusce vel massa nulla. Phasellus nec eros mauris, et scelerisque orci.</p>
    <p>Donec malesuada orci vitae nulla accumsan porta a id massa. Quisque accumsan iaculis magna sit amet fringilla. Maecenas consequat, magna eget tincidunt semper, odio nibh rutrum mi, id feugiat ante nisi eu risus. Vestibulum nunc orci, rhoncus a placerat in, ultricies in mi. Cras mattis varius eros, vel fringilla nisi suscipit eget. Quisque scelerisque sagittis nulla at porttitor.</p>
    <p>Sed id augue vitae urna euismod commodo aliquet a quam. Pellentesque arcu velit, cursus et malesuada ut, consequat et diam. Nullam erat sem, rhoncus id ullamcorper vitae, rhoncus et arcu. In ultricies ultricies nulla, ut rutrum nisi iaculis at. Donec eu magna a metus ornare faucibus. Fusce aliquet faucibus ultricies. Morbi semper, est id tincidunt gravida, sem arcu adipiscing lacus, ac bibendum nulla leo eu purus. Quisque nec diam sed risus consectetur a cursus quis quis nibh. Vestibulum id purus lorem.</p>
    <p>It is a long established fact that a reader will be distracted by the readable content of a page when looking at its layout. The point of using Lorem Ipsum is that it has a more-or-less normal distribution of letters, as opposed to using 'Content here, content here', making it look like readable English. Many desktop publishing packages</p>
    <p style="margin-top:12px">Sincerely,</p>
  </div>
  <div class="signature" role="img" aria-label="Handwritten signature"></div>
  <div class="footer" style="top:401px">Level 1, 214 Garrow Street, Brackenvale NSW 2316<br>National Provider Number 7192 | ABN 53 614 289 117</div>
</section>

<section class="clear-card">
  <div class="logo" style="left:90px;top:13px"><i class="mark"></i><span class="name" style="font-size:10px">ironquill build</span></div>
  <div class="person" style="left:90px;top:32px"><b style="color:#1b1d24">DANIEL REEVE</b>CEO/FOUNDER</div>
  <div class="address" style="left:90px;top:48px;color:#25272d">1300 587 902<br>0438 761 205<br>name@ironquillbuild.com.au<br>www.ironquillbuild.com.au</div>
  <div class="footer" style="top:80px;padding-top:4px;font-size:4px;line-height:5px;color:#25272d;border-color:#6a6e76">Level 1, 214 Garrow Street, Brackenvale NSW 2316<br>National Provider Number 7192 | ABN 53 614 289 117</div>
</section>

<section class="sheet" style="left:370px;top:210px;width:312px;height:141px">
  <svg style="position:absolute;left:0;top:0" width="312" height="46" viewBox="0 0 312 46"><path d="M0 0H312L308 30Q306 44 292 44H20Q6 44 4 30Z" fill="var(--navy)"/></svg>
  <div class="logo white" style="left:116px;top:15px"><i class="mark"></i><span class="name" style="font-size:10px">ironquill build</span></div>
</section>

<section class="sheet" style="left:370px;top:370px;width:312px;height:141px">
  <div class="logo" style="left:17px;top:15px"><i class="mark"></i><span class="name" style="font-size:11px">ironquill build</span></div>
  <div class="address" style="left:17px;top:38px">Level 1, 214 Garrow Street<br>Brackenvale NSW 2316<br>National Provider Number 7192<br>ABN 53 614 289 117</div>
</section>

<section class="sheet" style="left:370px;top:528px;width:312px;height:142px">
  <div class="logo" style="left:17px;top:17px"><i class="mark"></i><span class="name" style="font-size:11px">ironquill build</span></div>
  <div class="contact" style="left:226px;top:14px">
    <span>1300 587 902</span><span>name@ironquillbuild.com.au</span><span>www.ironquillbuild.com.au</span>
  </div>
  <div class="compliments">With Compliments</div>
  <div class="footer" style="top:112px">Level 1, 214 Garrow Street, Brackenvale NSW 2316<br>National Provider Number 7192 | ABN 53 614 289 117</div>
</section>

<section class="sheet" style="left:42px;top:493px;width:310px;height:398px">
  <div class="spiral"></div>
  <div class="logo" style="left:27px;top:22px"><i class="mark"></i><span class="name">ironquill build</span></div>
  <div class="contact" style="left:210px;top:20px">
    <span>1300 587 902</span><span>name@ironquillbuild.com.au</span><span>www.ironquillbuild.com.au</span>
  </div>
  <div class="notebook-lines"></div>
  <div class="footer" style="top:363px">Level 1, 214 Garrow Street, Brackenvale NSW 2316<br>National Provider Number 7192 | ABN 53 614 289 117</div>
</section>

<section class="sheet" style="left:374px;top:689px;width:180px;height:94px">
  <div class="logo" style="left:14px;top:12px"><i class="mark"></i><span class="name" style="font-size:10px">ironquill build</span></div>
  <div class="person" style="left:90px;top:30px"><b>DANIEL REEVE</b>CEO/FOUNDER</div>
  <div class="address" style="left:90px;top:46px">1300 587 902<br>0438 761 205<br>name@ironquillbuild.com.au<br>www.ironquillbuild.com.au</div>
  <div class="footer" style="top:75px;padding-top:3px;font-size:4px;line-height:5px">Level 1, 214 Garrow Street, Brackenvale NSW 2316<br>National Provider Number 7192 | ABN 53 614 289 117</div>
</section>

<section class="sheet" style="left:374px;top:799px;width:180px;height:88px">
  <div class="logo" style="left:36px;top:13px"><i class="mark"></i><span class="name">ironquill build</span></div>
  <div class="person" style="left:38px;top:42px;text-align:right"><b>DANIEL REEVE</b>CEO/FOUNDER</div>
  <div class="address" style="left:86px;top:38px">1300 587 902<br>0438 761 205<br>name@ironquillbuild.com.au<br>www.ironquillbuild.com.au</div>
  <div class="footer" style="top:70px;padding-top:3px;font-size:4px;line-height:5px">Level 1, 214 Garrow Street, Brackenvale NSW 2316<br>National Provider Number 7192 | ABN 53 614 289 117</div>
</section>

<section class="sheet" style="left:571px;top:689px;width:111px;height:198px">
  <div class="logo" style="left:14px;top:97px"><i class="mark"></i><span class="name">ironquill build</span></div>
  <div class="person" style="left:14px;top:120px"><b>DANIEL REEVE</b>CEO/FOUNDER</div>
  <div class="address" style="left:14px;top:137px">1300 587 902<br>0438 761 205<br>name@ironquillbuild.com.au<br>www.ironquillbuild.com.au</div>
  <div class="footer" style="top:177px;padding-top:3px;font-size:3.6px;line-height:5px">Level 1, 214 Garrow Street, Brackenvale NSW 2316<br>National Provider Number 7192 | ABN 53 614 289 117</div>
</section>

<section class="sheet" style="left:709px;top:34px;width:282px;height:441px">
  <div class="band" style="left:0;top:0;width:282px;height:42px;border-radius:3px 3px 0 0"></div>
  <div class="logo" style="left:14px;top:57px"><i class="mark"></i><span class="name">ironquill build</span></div>
  <div class="address" style="left:14px;top:79px">Level 1, 214 Garrow Street<br>Brackenvale NSW 2316<br>National Provider Number 7192<br>ABN 53 614 289 117</div>
</section>

<section class="sheet" style="left:709px;top:497px;width:441px;height:281px">
  <div class="band" style="left:400px;top:0;width:41px;height:281px;border-radius:0 4px 4px 0"></div>
  <div class="logo" style="left:18px;top:18px"><i class="mark"></i><span class="name">ironquill build</span></div>
  <div class="address" style="left:18px;top:39px">Level 1, 214 Garrow Street<br>Brackenvale NSW 2316<br>National Provider Number 7192<br>ABN 53 614 289 117</div>
</section>

</body>
</html>
```